Website Home Page for Women's Health Medical Office

Redesign existing homepage for website using existing logo. Current website location is www.lumawomenscare.com. Please give it a modern, streamlined, playful feel.

Please give it a feminine feel and make it bright and cheerful using logo colors.

Target Market(s)

Women between the ages of 25-45

Industry/Entity Type

Medical Office

Coding

Coded - Design and coding required

Number of Pages Required

1 page

Font styles to use
Sans Serif
Other font styles liked:
• SEGOI UI script for text and GIL SANS for bold (or their equivilent)

Colors
E54698
E96AAD
F1A4CE
F9D9EA
FCEFF6

Requirements
Must have
• Existing logo. Logo Colors. Feminine, cheerful, simple design. all relevant contact information
Nice to have
• clean lines and streamlined look
Should not have
• Cluttered

```html
<!DOCTYPE html>
<html lang="en">
<head>
<meta charset="utf-8">
<title>Luma OB/GYN — Personalized Medical Care For Women</title>
<link rel="stylesheet" href="https://fonts.googleapis.com/css2?family=Fira+Sans+Condensed:wght@300;400;500;600&family=Poppins:wght@400;500;600&family=Roboto:wght@300;400;500&display=swap">
<style>
  :root {
    --pink-hot: #f22e8c;
    --pink: #e54698;
    --pink-mid: #e96aad;
    --pink-soft: #f1a4ce;
    --pink-pale: #f9d9ea;
    --pink-mist: #fceff6;
    --ink: #111111;
    --text-grey: #555555;
    --white: #ffffff;
    --footer-bg: #f7f7f7;
  }
  * { margin: 0; padding: 0; box-sizing: border-box; }
  html, body { width: 1200px; height: 2783px; overflow: hidden; }
  body { position: relative; background: var(--white); font-family: "Fira Sans Condensed", sans-serif; color: var(--ink); }
  .abs { position: absolute; }

  /* Top bar */
  .topbar { left: 0; top: 0; width: 1200px; height: 38px; background: var(--pink-hot); display: flex; justify-content: center; align-items: center; gap: 28px; color: var(--white); font-size: 15px; }
  .topbar span { display: flex; align-items: center; gap: 6px; }
  .topbar svg { width: 11px; height: 11px; fill: var(--white); }

  /* Nav */
  .nav { left: 0; top: 38px; width: 1200px; height: 104px; border-bottom: 3px solid var(--pink-hot); background: var(--white); }
  .brand { left: 146px; top: 36px; display: flex; align-items: center; gap: 7px; font-family: "Poppins", sans-serif; font-weight: 600; font-size: 17px; color: var(--pink); }
  .brand i { width: 12px; height: 12px; border-radius: 50%; background: var(--pink); display: block; }
  .menu a { position: absolute; top: 44px; font-size: 18px; color: #222; text-decoration: none; }
  .menu a.active { color: var(--pink-hot); }
  .social { position: absolute; top: 46px; width: 16px; height: 16px; border-radius: 50%; background: var(--pink-hot); }

  /* Hero */
  .hero { left: 0; top: 142px; width: 1200px; height: 601px; background: linear-gradient(115deg, #e2b2cc 0%, #f3d6e5 35%, #f6e2ec 55%, #e7b2cf 100%); overflow: hidden; }
  .hero-photo { left: 690px; top: 20px; width: 390px; height: 581px; border-radius: 190px 190px 0 0; background: radial-gradient(ellipse at 50% 40%, #e9e9e2 0%, #cfd5cf 45%, #d9a9c3 100%); }
  .welcome { left: 141px; top: 175px; font-family: "Poppins", sans-serif; font-size: 27px; color: var(--ink); }
  .hero-title { left: 140px; top: 205px; font-family: "Poppins", sans-serif; font-weight: 600; font-size: 57px; line-height: 1.2; letter-spacing: 0.5px; color: var(--ink); }
  .hero-sub { left: 143px; top: 290px; font-size: 30px; color: #222; }
  .hero-tag { left: 143px; top: 330px; font-size: 17px; color: #222; }

  .btn { position: absolute; display: flex; align-items: center; justify-content: center; border-radius: 22px; font-weight: 600; font-size: 18px; color: var(--white); text-decoration: none; }
  .btn-pink { background: var(--pink-hot); }
  .btn-dark { background: var(--ink); }

  /* Pink bands */
  .band { left: 0; width: 1200px; background: var(--pink-hot); color: var(--white); }
  .photo { border-radius: 10px; }
  .band h2 { position: absolute; font-weight: 600; font-size: 40px; line-height: 38px; }
  .band p { position: absolute; font-weight: 300; font-size: 17.5px; line-height: 27px; text-align: justify; }

  /* Accepting */
  .accept-kicker { left: 0; top: 1199px; width: 1200px; text-align: center; font-weight: 600; font-size: 40px; color: var(--pink-hot); }
  .accept-title { left: 0; top: 1255px; width: 1200px; text-align: center; font-family: "Poppins", sans-serif; font-weight: 600; font-size: 47px; color: var(--ink); }

  /* Help */
  .help-title { left: 0; top: 1867px; width: 1200px; text-align: center; font-weight: 600; font-size: 40px; color: var(--pink-hot); }
  .card { top: 1955px; width: 218px; height: 483px; background: var(--white); box-shadow: 0 1px 8px rgba(0,0,0,0.09); text-align: center; }
  .card-icon { position: absolute; left: 79px; top: 29px; width: 60px; height: 60px; border-radius: 50%; background: var(--pink-pale); border: 2px solid var(--pink-hot); }
  .card h3 { position: absolute; left: 0; top: 108px; width: 218px; font-family: "Roboto", sans-serif; font-weight: 500; font-size: 15px; color: var(--ink); }
  .card p { position: absolute; left: 14px; top: 144px; width: 190px; font-family: "Roboto", sans-serif; font-weight: 300; font-size: 14.5px; line-height: 24px; color: var(--text-grey); }
  .card .btn { left: 41px; top: 420px; width: 136px; height: 34px; font-family: "Roboto", sans-serif; font-weight: 400; font-size: 15px; border-radius: 17px; }

  /* Footer */
  .footer { left: 0; top: 2498px; width: 1200px; height: 245px; background: var(--footer-bg); }
  .footer-brand { left: 150px; top: 100px; display: flex; align-items: center; gap: 8px; font-family: "Poppins", sans-serif; font-weight: 600; font-size: 24px; color: var(--pink); }
  .footer-brand i { width: 16px; height: 16px; background: var(--pink); display: block; }
  .footer ul { position: absolute; list-style: none; font-family: "Roboto", sans-serif; font-size: 18px; line-height: 29px; color: #222; top: 70px; }
  .contact { position: absolute; left: 845px; top: 66px; font-size: 16.5px; line-height: 27px; color: #222; }
  .contact div { display: flex; gap: 10px; }
  .contact svg { width: 11px; height: 11px; fill: #222; margin-top: 8px; flex: none; }
  .contact .indent { padding-left: 21px; }

  .bottombar { left: 0; top: 2743px; width: 1200px; height: 40px; background: var(--pink-hot); color: var(--white); font-family: "Roboto", sans-serif; font-size: 13px; display: flex; align-items: center; justify-content: center; }
</style>
</head>
<body>

<div class="abs topbar">
  <span><svg viewBox="0 0 10 10"><path d="M2 0l2 2-1 1.5c.6 1.4 1.6 2.4 3 3L7.5 5.5l2 2L8 9.5C4 9 1 6 .5 2z"/></svg>(555) 214-3380</span>
  <span><svg viewBox="0 0 10 10"><path d="M0 2h10v6H0zM1 3v.3l4 2.5 4-2.5V3z"/></svg>hello@lumawomenscare.com</span>
  <span><svg viewBox="0 0 10 10"><path d="M5 0a3.5 3.5 0 0 1 3.5 3.5C8.5 6 5 10 5 10S1.5 6 1.5 3.5A3.5 3.5 0 0 1 5 0zm0 2a1.5 1.5 0 1 0 0 3 1.5 1.5 0 0 0 0-3z"/></svg>1840 Willowbrook Lane, Suite 310, Fairhaven, CA 90210</span>
  <span><svg viewBox="0 0 10 10"><path d="M2 0h6v3H2zM0 4h10v4H8v2H2V8H0z"/></svg>555-214-3391</span>
</div>

<header class="abs nav">
  <div class="abs brand"><i></i>Luma OB/GYN</div>
  <nav class="menu">
    <a class="active" style="left:398px">Home</a>
    <a style="left:485px">About</a>
    <a style="left:573px">Services</a>
    <a style="left:673px">Resources</a>
    <a style="left:787px">Contact</a>
  </nav>
  <span class="social" style="left:966px"></span>
  <span class="social" style="left:996px"></span>
  <span class="social" style="left:1030px"></span>
</header>

<section class="abs hero">
  <div class="abs hero-photo" role="img" aria-label="Photo of a smiling pregnant woman in a light grey top holding her belly"></div>
  <div class="abs welcome">Welcome to</div>
  <h1 class="abs hero-title">LUMA OB/GYN</h1>
  <div class="abs hero-sub">Personalized Medical Care For Women</div>
  <div class="abs hero-tag">Better Health Starts Here!</div>
  <a class="btn btn-pink" style="left:141px;top:381px;width:148px;height:40px">Get Started</a>
</section>

<section class="abs band" style="top:743px;height:400px">
  <div class="abs photo" role="img" aria-label="Portrait photo of a smiling physician in navy scrubs" style="left:144px;top:34px;width:280px;height:329px;background:linear-gradient(160deg,#6d7a8e,#3d475c 60%,#1f2a45)"></div>
  <h2 style="left:462px;top:62px;width:600px">Serving Willowbrook Medical Center</h2>
  <p style="left:469px;top:157px;width:580px">At Luma OB/GYN in Fairhaven, California, we believe better health starts when the patient is educated. For this reason, we take time to listen to our patients concerns, explain each option available, and to answer any questions our patients may have so that they can make informed decisions. At Luma OB/GYN, our providers tailor every procedure performed and treatment option recommended to meet the specific needs of our patients.</p>
  <a class="btn btn-dark" style="left:463px;top:339px;width:148px;height:40px">Read More</a>
</section>

<div class="abs accept-kicker">Better Health Starts Here!</div>
<div class="abs accept-title">NOW ACCEPTING NEW PATIENTS</div>
<a class="btn btn-pink" style="left:488px;top:1333px;width:225px;height:40px">Schedule An Appointment</a>

<section class="abs band" style="top:1420px;height:400px">
  <h2 style="left:145px;top:57px;width:600px">Your OB/GYN Specialists</h2>
  <p style="left:146px;top:112px;width:614px">Luma OB/GYN offers you the best care possible in a personalized setting. We are currently accepting patients. Call our office now to make an appointment.</p>
  <p style="left:146px;top:193px;width:614px">Luma OB/GYN (located near Willowbrook Hospital in Fairhaven, CA) is a medical office that specializes in Christ-centered healthcare for women of all ages. Our team of exclusively female providers have years of experience taking care of women with a variety of pregnancy and gynecology concerns.</p>
  <a class="btn btn-dark" style="left:145px;top:325px;width:148px;height:40px">Read More</a>
  <div class="abs photo" role="img" aria-label="Photo of a smiling provider in blue scrubs holding a newborn in a hospital room" style="left:772px;top:34px;width:281px;height:329px;background:linear-gradient(160deg,#c9b69a,#9fb6c8 55%,#e0b3a8)"></div>
</section>

<h2 class="abs help-title">How Can We Help You?</h2>

<div class="abs card" style="left:144px">
  <div class="card-icon" role="img" aria-label="Pregnancy care icon"></div>
  <h3>PREGNANCY CARE</h3>
  <p>Receiving regular care in pregnancy is important for the health of both you and your baby. Our obstetrcians work with you every step of the way during your pregnancy and delivery to make sure your individual needs are met and co ensure this special journey is a memorable one.</p>
  <a class="btn btn-pink">Learn More</a>
</div>
<div class="abs card" style="left:374px">
  <div class="card-icon" role="img" aria-label="Birth control icon"></div>
  <h3>BIRTH CONTROL</h3>
  <p>Our gynecologists are knowledgeable on all forms of birth control including the IUD, arm implant, vaginal ringinsertion, birth control pills, and more! We would love to work with you to determine the best option for you and your lifestyle.</p>
  <a class="btn btn-pink">Learn More</a>
</div>
<div class="abs card" style="left:605px">
  <div class="card-icon" role="img" aria-label="Well woman exam icon"></div>
  <h3>WELL WOMAN EXAMS</h3>
  <p>Our providers will help you to stay healthy by performing a physical exam on you annually. We will screen you for multiple health conditions that may pose a risk to you. This includes screening you for cancerous conditions of the breast, ovaries and cervix.</p>
  <a class="btn btn-pink">Learn More</a>
</div>
<div class="abs card" style="left:835px">
  <div class="card-icon" role="img" aria-label="Women's health icon"></div>
  <h3>WOMEN'S HEALTH</h3>
  <p>Whether you are dealing with painful or irregular periods, fibroids, or other women's health i ssues, we can help. We offer a variety of the most up-to-date treatment options to help you regain your lifestyle.</p>
  <a class="btn btn-pink">Learn More</a>
</div>

<footer class="abs footer">
  <div class="abs footer-brand"><i></i>Luma OB/GYN</div>
  <ul style="left:410px"><li>Home</li><li>About Us</li><li>News</li><li>Patient Resources</li></ul>
  <ul style="left:614px"><li>Privacy Policy</li><li>Contact us</li><li>Terms &amp; Conditions</li><li>Support</li></ul>
  <div class="contact">
    <div><svg viewBox="0 0 10 10"><path d="M2 0l2 2-1 1.5c.6 1.4 1.6 2.4 3 3L7.5 5.5l2 2L8 9.5C4 9 1 6 .5 2z"/></svg>(555) 214-3380</div>
    <div><svg viewBox="0 0 10 10"><path d="M0 2h10v6H0zM1 3v.3l4 2.5 4-2.5V3z"/></svg>hello@lumawomenscare.com</div>
    <div><svg viewBox="0 0 10 10"><path d="M5 0a3.5 3.5 0 0 1 3.5 3.5C8.5 6 5 10 5 10S1.5 6 1.5 3.5A3.5 3.5 0 0 1 5 0zm0 2a1.5 1.5 0 1 0 0 3 1.5 1.5 0 0 0 0-3z"/></svg>1840 Willowbrook Lane,</div>
    <div class="indent">Suite 310, Fairhaven, CA 90210</div>
    <div><svg viewBox="0 0 10 10"><path d="M2 0h6v3H2zM0 4h10v4H8v2H2V8H0z"/></svg>555-214-3391</div>
  </div>
</footer>

<div class="abs bottombar">© copyrights 2022 Luma OB/GYN | &nbsp;All Rights Reserved</div>

</body>
</html>
```